Hot young IT advisor needs business cards as upscale and innovative as they are

We need business cards that make a statement about who we are, as a young and upscale IT advisor. Our whole angle is innovation and tenacity in our personal relationships with our clients. We've just done a brand overhaul and need cards that have the new logos, but we're also looking for someone with a sixth sense who can capture what sets us apart and communicate that with a business card. Clean, minimalist, upscale, innovative, personal. Our budget only allows room for them to be soft-touch, no spot gloss or foil designs please.

Target Market(s)

High-level decision makers at middle-market and large organizations in the healthcare, financial services, sports and entertainment, K-12 education, college and university, state and local government, and federal government sectors.

Industry/Entity Type

Information Technology

Font styles to use
Sans Serif

Colors
ec1f27
606060
ffffff

Requirements
Should not have
• Designs with low contrast which would require spot-gloss or embossing.

```html
<!DOCTYPE html>
<html lang="en">
<head>
<meta charset="utf-8">
<title>Velnora Business Card</title>
<link rel="stylesheet" href="https://fonts.googleapis.com/css2?family=Montserrat:wght@400;500&display=swap">
<style>
  :root {
    --brand-red: #e3263f;
    --accent-red: #ec1f27;
    --ink: #333333;
    --band-dark: #363834;
    --paper: #ffffff;
    --backdrop: #3a3b3e;
  }
  * { margin: 0; padding: 0; box-sizing: border-box; }
  html, body {
    width: 1200px;
    height: 900px;
    overflow: hidden;
    background: var(--backdrop);
    font-family: "Montserrat", sans-serif;
  }
  .canvas {
    position: relative;
    width: 1200px;
    height: 900px;
  }
  .card {
    position: absolute;
    width: 560px;
    height: 320px;
    border-radius: 26px;
    overflow: hidden;
  }
  .card--front {
    left: 90px;
    top: 110px;
    background: var(--brand-red);
  }
  .card--back {
    left: 550px;
    top: 470px;
    background: var(--paper);
  }
  .front-wordmark {
    position: absolute;
    left: 0;
    right: 0;
    top: 50%;
    transform: translateY(-50%);
    text-align: center;
    color: var(--paper);
    font-weight: 400;
    font-size: 46px;
    letter-spacing: 6px;
  }
  .back-wordmark {
    position: absolute;
    left: 58px;
    top: 150px;
    color: var(--ink);
    font-weight: 400;
    font-size: 24px;
    letter-spacing: 3px;
  }
  .holder-name {
    position: absolute;
    left: 300px;
    top: 52px;
    font-size: 22px;
    font-weight: 400;
    letter-spacing: 2px;
    color: var(--ink);
  }
  .holder-name__last { color: var(--accent-red); }
  .contact-icons {
    position: absolute;
    left: 300px;
    top: 110px;
    display: flex;
    flex-direction: column;
    gap: 14px;
  }
  .contact-icons svg { width: 16px; height: 16px; display: block; }
  .card-bands {
    position: absolute;
    left: 0;
    top: 0;
  }
</style>
</head>
<body>
<main class="canvas">
  <section class="card card--front">
    <p class="front-wordmark">VELNORA</p>
  </section>

  <section class="card card--back">
    <p class="holder-name">FULL <span class="holder-name__last">NAME</span></p>
    <p class="back-wordmark">VELNORA</p>

    <div class="contact-icons">
      <svg viewBox="0 0 16 16" aria-label="Phone">
        <path fill="var(--accent-red)" d="M3 1.5l2.5-.5 1.5 3.5-1.8 1.2a8 8 0 0 0 4.6 4.6L11 8.5l3.5 1.5-.5 2.5c-.3 1.2-1.5 2-2.7 1.6C6.8 12.8 3.2 9.2 1.9 4.7 1.5 3.5 2 2.1 3 1.5z"/>
      </svg>
      <svg viewBox="0 0 16 16" aria-label="Address">
        <path fill="var(--accent-red)" d="M8 1a5 5 0 0 0-5 5c0 3.6 5 9 5 9s5-5.4 5-9a5 5 0 0 0-5-5zm0 7a2 2 0 1 1 0-4 2 2 0 0 1 0 4z"/>
      </svg>
      <svg viewBox="0 0 16 16" aria-label="Email">
        <rect x="1" y="3.5" width="14" height="9" fill="var(--accent-red)"/>
        <path d="M1.5 4l6.5 5 6.5-5" fill="none" stroke="var(--paper)" stroke-width="1"/>
      </svg>
      <svg viewBox="0 0 16 16" aria-label="Website">
        <circle cx="8" cy="8" r="7" fill="var(--accent-red)"/>
        <g fill="none" stroke="var(--paper)" stroke-width="0.8">
          <ellipse cx="8" cy="8" rx="3" ry="7"/>
          <line x1="1" y1="8" x2="15" y2="8"/>
          <line x1="8" y1="1" x2="8" y2="15"/>
          <path d="M2.5 4.5h11M2.5 11.5h11"/>
        </g>
      </svg>
    </div>

    <svg class="card-bands" width="560" height="320" viewBox="0 0 560 320" aria-hidden="true">
      <path d="M0 262 H330 Q336 262 338 256 L340 250 H0 Z" fill="var(--accent-red)" transform="translate(0,6)"/>
      <path d="M350 262 Q350 240 372 236 H560 V254 H372 Q360 254 358 262 Z" fill="var(--band-dark)" transform="translate(0,-10)"/>
    </svg>
  </section>
</main>
</body>
</html>
```